Crimson Vantage Cleaning Solutions

Need a logo and business card design. I want to use a translucent business card. I want to abbreviate the name Crimson Vantage Cleaning Solutions, because my is Dov. I’d also like to incorporate a knight or something like that. I want the idea to tie in with the word Crimson. New ideas are welcome, i don’t want to limit anyone’s creativity.

Target Market(s)

Commercial Cleaning for businesses.

Contact Information for Business Card

Crimson
Vantage
Cleaning
Solutions

```html
<!DOCTYPE html>
<html lang="en">
<head>
<meta charset="utf-8">
<title>Crimson Vantage Cleaning Solutions – Business Card</title>
<link rel="stylesheet" href="https://fonts.googleapis.com/css2?family=Work+Sans:wght@400;500&display=swap">
<style>
  :root {
    --page-bg: #e9e4dc;
    --card-frost: #f4f1ec;
    --card-edge: #d9d3ca;
    --ink: #2b2826;
    --ink-soft: #3a3633;
    --band: #1f1d1c;
  }
  html, body {
    margin: 0;
    width: 1200px;
    height: 1047px;
    overflow: hidden;
    background: var(--page-bg);
    font-family: "Work Sans", Arial, sans-serif;
  }
  .business-card {
    position: absolute;
    left: 100px;
    top: 251px;
    width: 1000px;
    height: 545px;
    border-radius: 24px;
    background: linear-gradient(160deg, #f8f6f2 0%, var(--card-frost) 55%, #ece8e1 100%);
    box-shadow: inset 0 0 0 1px var(--card-edge), 0 10px 30px rgba(60, 50, 40, 0.12);
    overflow: hidden;
    color: var(--ink);
  }
  .brand {
    position: absolute;
    left: 80px;
    top: 222px;
    display: flex;
    align-items: center;
    gap: 22px;
  }
  .brand-dot {
    width: 74px;
    height: 74px;
    border-radius: 50%;
    background: var(--ink-soft);
    flex: none;
  }
  .brand-name {
    margin: 0;
    font-size: 33px;
    font-weight: 500;
    line-height: 1.2;
    letter-spacing: 0.5px;
    color: var(--ink-soft);
  }
  .divider {
    position: absolute;
    left: 580px;
    top: 153px;
    width: 2px;
    height: 240px;
    background: var(--ink);
  }
  .contact {
    position: absolute;
    left: 641px;
    top: 143px;
    font-size: 23px;
    letter-spacing: 0.6px;
    color: var(--ink);
  }
  .contact .person-name {
    margin: 0;
    font-size: 29px;
    font-weight: 500;
    letter-spacing: 1.2px;
    text-transform: uppercase;
  }
  .contact .person-role { margin: 4px 0 0; }
  .contact .address { margin: 22px 0 0; line-height: 1.4; font-style: normal; }
  .contact .lines { list-style: none; margin: 20px 0 0; padding: 0; }
  .contact .lines li {
    display: flex;
    align-items: center;
    gap: 14px;
    line-height: 1.42;
  }
  .contact .lines svg { width: 16px; height: 16px; flex: none; }
  .bottom-band {
    position: absolute;
    left: 0;
    bottom: 0;
    width: 1000px;
    height: 50px;
  }
</style>
</head>
<body>
  <main class="business-card">
    <div class="brand">
      <span class="brand-dot"></span>
      <p class="brand-name">Crimson Vantage<br>Cleaning Solutions</p>
    </div>

    <span class="divider"></span>

    <section class="contact">
      <h1 class="person-name">Dana Whitfield</h1>
      <p class="person-role">Director</p>
      <address class="address">312 Harbor Oak Drive<br>Seabrook, TX 77586</address>
      <ul class="lines">
        <li>
          <svg viewBox="0 0 16 16" aria-hidden="true"><path d="M4 1.5 6.2 4.3 4.9 6a8 8 0 0 0 5 5l1.7-1.3 2.9 2.2-1.4 2.1C8 14 2 8 1.9 2.9Z" fill="var(--ink)"/></svg>
          <span>281-555-0147</span>
        </li>
        <li>
          <svg viewBox="0 0 16 16" aria-hidden="true"><rect x="2" y="4" width="12" height="9" fill="none" stroke="var(--ink)" stroke-width="1.4"/><path d="M2 4.5 8 9l6-4.5" fill="none" stroke="var(--ink)" stroke-width="1.4"/></svg>
          <span>info@cvcs-clean.com</span>
        </li>
        <li>
          <svg viewBox="0 0 16 16" aria-hidden="true"><circle cx="8" cy="8" r="6" fill="none" stroke="var(--ink)" stroke-width="1.3"/><ellipse cx="8" cy="8" rx="2.6" ry="6" fill="none" stroke="var(--ink)" stroke-width="1.1"/><path d="M2 8h12" stroke="var(--ink)" stroke-width="1.1"/></svg>
          <span>www.cvcs-clean.com</span>
        </li>
      </ul>
    </section>

    <svg class="bottom-band" viewBox="0 0 1000 50" aria-hidden="true">
      <rect x="0" y="16" width="600" height="6" fill="var(--band)"/>
      <path d="M0 32 H600 C620 32 625 10 650 10 H1000 V50 H0 Z" fill="var(--band)"/>
    </svg>
  </main>
</body>
</html>
```